Business Card Design

We need a business card design for a Dry cleaners in Brisbane, Australia. We are trying to promote a fresh/clean image consistent with our website. www.finchlanelaundry.com.au

Looking for a professional neat card that's easy to read.

Target Market(s)

Customers looking for a professional, fresh and clean drycleaners.

Industry/Entity Type

Business

Contact Information for Business Card

See our existing business card. The Fax number (07) 3648 2051 to be removed.

Requirements
Must have
• All the details on current business card less the fax number.
Nice to have
• I like white text on coloured background. Blue works well as we are located near the water...

```html
<!DOCTYPE html>
<html lang="en">
<head>
<meta charset="utf-8">
<title>Finch Lane Laundry – Business Card</title>
<link rel="stylesheet" href="https://fonts.googleapis.com/css2?family=Exo+2:wght@400;600;700&display=swap">
<style>
  :root {
    --page-bg: #ece9e4;
    --card-white: #ffffff;
    --card-fade: #eef0f3;
    --brand-blue: #34399a;
    --brand-red: #ec2a36;
    --ink: #3a3d4a;
    --rule: #9a9da8;
  }
  * { box-sizing: border-box; margin: 0; padding: 0; }
  html, body {
    width: 1200px; height: 677px; overflow: hidden;
    background: var(--page-bg);
    font-family: "Exo 2", sans-serif;
  }
  .stage {
    width: 1200px; height: 677px;
    display: flex; align-items: center; justify-content: center;
  }
  .card {
    width: 350px; height: 580px;
    border: 9px solid var(--brand-blue);
    background: linear-gradient(180deg, var(--card-white) 0%, var(--card-white) 55%, var(--card-fade) 100%);
    position: relative;
    box-shadow: 0 8px 24px rgba(0,0,0,0.18);
  }
  .brand {
    position: absolute; top: 88px; left: 0; right: 0;
    display: flex; align-items: center; justify-content: center; gap: 10px;
  }
  .brand-dot {
    width: 14px; height: 14px; border-radius: 50%;
    background: var(--brand-red);
  }
  .brand-name {
    font-weight: 700; font-size: 28px; color: var(--brand-blue);
    letter-spacing: 0.5px;
  }
  .name-band {
    position: absolute; top: 170px; left: 0; right: 0; height: 74px;
    background: var(--brand-red); color: #fff;
    display: flex; flex-direction: column; justify-content: center;
    padding-left: 26px;
  }
  .person-name { font-size: 22px; font-weight: 400; letter-spacing: 2px; text-transform: uppercase; }
  .person-title { font-size: 16px; font-weight: 400; letter-spacing: 1.5px; text-transform: uppercase; }
  .contacts {
    position: absolute; top: 276px; left: 22px; right: 22px;
    list-style: none;
  }
  .contact {
    display: flex; align-items: center; gap: 12px;
    font-size: 13px; color: var(--ink); height: 34px;
  }
  .icon-box {
    width: 20px; height: 20px; border-radius: 3px;
    background: var(--brand-blue); flex: none;
    display: flex; align-items: center; justify-content: center;
  }
  .icon-box svg { width: 13px; height: 13px; }
  .address-rule {
    position: absolute; top: 428px; left: 0; right: 0;
    border-top: 1.5px solid var(--rule);
  }
  .address {
    position: absolute; top: 440px; left: 22px; right: 22px;
  }
  .bottom-rule {
    position: absolute; top: 486px; left: 0; right: 0;
    border-top: 1.5px solid var(--rule);
  }
</style>
</head>
<body>
<main class="stage">
  <article class="card">
    <div class="brand">
      <span class="brand-dot"></span>
      <span class="brand-name">Finch Lane Laundry</span>
    </div>

    <div class="name-band">
      <span class="person-name">Mara Ellison</span>
      <span class="person-title">General Manager</span>
    </div>

    <ul class="contacts">
      <li class="contact">
        <span class="icon-box"><svg viewBox="0 0 24 24"><path fill="#fff" d="M6.6 10.8a15.1 15.1 0 0 0 6.6 6.6l2.2-2.2a1 1 0 0 1 1-.25 11.4 11.4 0 0 0 3.6.57 1 1 0 0 1 1 1V20a1 1 0 0 1-1 1A17 17 0 0 1 3 4a1 1 0 0 1 1-1h3.5a1 1 0 0 1 1 1c0 1.25.2 2.450.57 3.57a1 1 0 0 1-.25 1z"/></svg></span>
        <span>(07) 3275 4418</span>
      </li>
      <li class="contact">
        <span class="icon-box"><svg viewBox="0 0 24 24"><rect x="6" y="2" width="12" height="20" rx="2" fill="#fff"/><rect x="8" y="5" width="8" height="12" fill="#34399a"/><circle cx="12" cy="19.5" r="1" fill="#34399a"/></svg></span>
        <span>0412 556 730</span>
      </li>
      <li class="contact">
        <span class="icon-box"><svg viewBox="0 0 24 24"><rect x="2" y="5" width="20" height="14" rx="1.5" fill="#fff"/><path d="M3 6l9 7 9-7" fill="none" stroke="#34399a" stroke-width="2"/></svg></span>
        <span>mara@finchlanelaundry.com.au</span>
      </li>
      <li class="contact">
        <span class="icon-box"><svg viewBox="0 0 24 24"><g fill="none" stroke="#fff" stroke-width="2"><circle cx="12" cy="12" r="9"/><ellipse cx="12" cy="12" rx="4" ry="9"/><path d="M3 12h18"/></g></svg></span>
        <span>www.finchlanelaundry.com.au</span>
      </li>
    </ul>

    <div class="address-rule"></div>
    <div class="address contact">
      <span class="icon-box"><svg viewBox="0 0 24 24"><path fill="#fff" d="M12 2a7 7 0 0 0-7 7c0 5 7 13 7 13s7-8 7-13a7 7 0 0 0-7-7zm0 9.5A2.5 2.5 0 1 1 12 6.5a2.5 2.5 0 0 1 0 5z"/></svg></span>
      <span>27 Wharf Street, Brisbane QLD</span>
    </div>
    <div class="bottom-rule"></div>
  </article>
</main>
</body>
</html>
```